Simple and Clean business card design

We would like the design to be simple clean and to incorporate our colors.

We are open to your design and talent, we have the dots in our logo as we think of it as data points and we connect data points for people.

We are open to see the great creative and clean design you bring to the table

Contact Information for Business Card

please include: name, position, email, phone and website

Font styles to use
Sans Serif

Requirements
Must have
• my colors incorporated, simplicity
Nice to have
• lots of white space, simplicity
Should not have
• complexicity/ complex art

```html
<!DOCTYPE html>
<html lang="en">
<head>
<meta charset="utf-8">
<title>Tandem business card</title>
<link rel="stylesheet" href="https://fonts.googleapis.com/css2?family=Montserrat:wght@400;500;700&display=swap">
<style>
  :root {
    --ink: #111111;
    --text: #333333;
    --rule: #8a8a8a;
    --blue: #5b84c4;
    --green: #3aa556;
    --yellow: #f5bf23;
    --red: #e2453a;
    --paper: #ffffff;
    --backdrop: #e9e6e1;
  }
  * { box-sizing: border-box; margin: 0; padding: 0; }
  html, body { width: 807px; height: 1200px; overflow: hidden; }
  body {
    background: var(--backdrop);
    font-family: "Montserrat", sans-serif;
    color: var(--text);
    display: flex;
    flex-direction: column;
    align-items: center;
    justify-content: center;
    gap: 60px;
  }
  .card {
    position: relative;
    width: 680px;
    height: 389px;
    background: var(--paper);
    border-radius: 10px;
    overflow: hidden;
    box-shadow: 0 6px 18px rgba(0,0,0,0.12);
  }
  .color-band {
    position: absolute;
    left: 0; right: 0; bottom: 0;
    height: 12px;
    display: flex;
  }
  .color-band span { flex: 1; }
  .color-band .blue { background: var(--blue); }
  .color-band .green { background: var(--green); }
  .color-band .yellow { background: var(--yellow); }
  .color-band .red { background: var(--red); }

  .wordmark {
    font-weight: 700;
    color: var(--ink);
    letter-spacing: -0.5px;
    display: flex;
    align-items: center;
    gap: 14px;
    line-height: 1;
  }
  .wordmark .dot {
    border-radius: 50%;
    background: var(--blue);
  }
  .card-front .wordmark {
    position: absolute;
    left: 50%; top: 46%;
    transform: translate(-50%, -50%);
    font-size: 92px;
  }
  .card-front .wordmark .dot { width: 40px; height: 40px; }

  .card-back .wordmark {
    position: absolute;
    right: 40px; top: 72px;
    font-size: 60px;
    gap: 10px;
  }
  .card-back .wordmark .dot { width: 26px; height: 26px; }

  .identity {
    position: absolute;
    left: 40px; top: 166px;
  }
  .identity .name {
    font-weight: 700;
    font-size: 22px;
    color: var(--ink);
    letter-spacing: 0.3px;
  }
  .identity .role {
    font-size: 15px;
    margin-top: 2px;
  }
  .divider {
    position: absolute;
    left: 40px; right: 40px; top: 240px;
    border-top: 1px solid var(--rule);
  }
  .contacts {
    position: absolute;
    left: 40px; top: 256px;
    list-style: none;
    font-size: 15px;
    line-height: 22px;
  }
  .contacts li { display: flex; align-items: center; gap: 10px; }
  .contacts svg { width: 14px; height: 14px; flex: none; }
  .address {
    position: absolute;
    right: 40px; top: 256px;
    text-align: right;
    font-size: 15px;
    line-height: 22px;
  }
  .address .company { font-weight: 700; color: var(--text); }
</style>
</head>
<body>

  <section class="card card-front">
    <div class="wordmark"><span class="dot"></span>Tandem</div>
    <div class="color-band"><span class="blue"></span><span class="green"></span><span class="yellow"></span><span class="red"></span></div>
  </section>

  <section class="card card-back">
    <div class="wordmark"><span class="dot"></span>Tandem</div>

    <div class="identity">
      <p class="name">DANIEL REYES</p>
      <p class="role">Founder/ CEO</p>
    </div>

    <div class="divider"></div>

    <ul class="contacts">
      <li>
        <svg viewBox="0 0 24 24"><path fill="#5b84c4" d="M6.6 10.8a15 15 0 0 0 6.6 6.6l2.2-2.2a1 1 0 0 1 1-.25 11.4 11.4 0 0 0 3.6.57 1 1 0 0 1 1 1V20a1 1 0 0 1-1 1A17 17 0 0 1 3 4a1 1 0 0 1 1-1h3.5a1 1 0 0 1 1 1c0 1.25.2 2.45.57 3.57a1 1 0 0 1-.25 1z"/></svg>
        555-214-3098
      </li>
      <li>
        <svg viewBox="0 0 24 24"><rect x="2" y="5" width="20" height="14" fill="#e2453a"/><path d="M2 5l10 8 10-8" fill="none" stroke="#fff" stroke-width="2"/></svg>
        lena.marsh@tandem.one
      </li>
      <li>
        <svg viewBox="0 0 24 24" fill="none" stroke="#3aa556" stroke-width="2"><circle cx="12" cy="12" r="10"/><path d="M2 12h20M12 2a15 15 0 0 1 0 20M12 2a15 15 0 0 0 0 20"/></svg>
        www.Tandem.one
      </li>
    </ul>

    <div class="address">
      <p class="company">Tandem.One</p>
      <p>Co. Street, Building, Suite</p>
      <p>State, Zip Code, Country</p>
    </div>

    <div class="color-band"><span class="blue"></span><span class="green"></span><span class="yellow"></span><span class="red"></span></div>
  </section>

</body>
</html>
```